Corvane Holdings needs a business card

I would like the card to be simple but modern and elegant.
I like black and white.
or black and gold.
we are a private finance lender and also are involved in property and property developments.

please look at the business card photos i provided i would like C.H only one one side and all the other details on the other side use fonts that tie in with my theme.

Industry/Entity Type

Finance

Contact Information for Business Card

Corvane Holdings (C.H) Elliot Marbury M: 0413586102 E: elliotmar@examplemail.net

Font styles to use
Other font styles liked:
• Use fonts that would reflect our business

Colors
000000
ffffff

Requirements
Must have
• one side of details
• other side has either C.H or Corvane Holdings like in the photos provided

```html
<!DOCTYPE html>
<html lang="en">
<head>
<meta charset="utf-8">
<title>Corvane Holdings — Business Card</title>
<link href="https://fonts.googleapis.com/css2?family=Cinzel:wght@400;700&family=Lato:wght@400&display=swap" rel="stylesheet">
<style>
  :root {
    --backdrop: #7f7f7f;
    --card-light: #ffffff;
    --card-light-edge: #ececee;
    --card-dark: #2a2a2b;
    --ink: #111111;
    --rule: #9a9a9a;
    --silver: #e4e4e4;
  }
  * { margin: 0; padding: 0; box-sizing: border-box; }
  html, body { width: 1200px; height: 900px; overflow: hidden; }
  body { background: var(--backdrop); position: relative; }

  .card {
    position: absolute;
    top: 271px;
    width: 457px;
    height: 281px;
  }

  .card-front {
    left: 137px;
    background: linear-gradient(90deg, var(--card-light) 0%, var(--card-light) 45%, var(--card-light-edge) 100%);
    color: var(--ink);
    text-align: center;
  }

  .brand-mark {
    position: absolute;
    left: 50%;
    top: 52px;
    width: 30px;
    height: 30px;
    margin-left: -15px;
    border: 2px solid var(--ink);
  }

  .company-name {
    position: absolute;
    top: 117px;
    left: 0;
    width: 100%;
    font-family: "Cinzel", serif;
    font-weight: 400;
    font-size: 29px;
    letter-spacing: 0.5px;
  }

  .person-name {
    position: absolute;
    top: 189px;
    left: 0;
    width: 100%;
    font-family: "Cinzel", serif;
    font-weight: 700;
    font-size: 16px;
    letter-spacing: 0.8px;
  }

  .divider {
    position: absolute;
    top: 218px;
    left: 150px;
    width: 157px;
    height: 1px;
    background: linear-gradient(90deg, transparent, var(--rule), transparent);
  }

  .contact-line {
    position: absolute;
    top: 228px;
    left: 0;
    width: 100%;
    font-family: "Lato", sans-serif;
    font-size: 13px;
  }
  .contact-line .sep { margin: 0 4px 0 8px; }

  .card-back {
    left: 626px;
    background: var(--card-dark);
  }

  .back-surface {
    position: absolute;
    inset: 0;
    background: radial-gradient(ellipse at 50% 50%, #323233 0%, var(--card-dark) 100%);
  }

  .back-initials {
    position: absolute;
    top: 0;
    left: 0;
    width: 100%;
    height: 100%;
    display: flex;
    align-items: center;
    justify-content: center;
    font-family: "Cinzel", serif;
    font-weight: 400;
    font-size: 64px;
    letter-spacing: 4px;
    color: var(--silver);
  }
</style>
</head>
<body>
  <section class="card card-front">
    <div class="brand-mark"></div>
    <h1 class="company-name">Corvane Holdings</h1>
    <h2 class="person-name">ELLIOT MARBURY</h2>
    <div class="divider"></div>
    <p class="contact-line">M: 0413586102 <span class="sep">|</span>E: elliotmar@examplemail.net</p>
  </section>

  <section class="card card-back">
    <div class="back-surface" role="img" aria-label="Black leather-textured card surface"></div>
    <div class="back-initials">C.H</div>
  </section>
</body>
</html>
```